Commercial and Residential Paint Contractor needs website

We need a website for our residential painting, multi-family painting and commercial painting company. We paint interior and exterior of houses, apartments and commercial buildings. I would like an about us page, residential page, multi family page, commercial page and contact us. Need keywords added to website for seo opitimazation. I like this website https://www.velmorandhalestudio.com/

Target Market(s)

General Contractors and commercial property managers

Coding

Coded - Design and coding required

Number of Pages Required

5+ page

Font styles to use
Sans Serif

Requirements
Must have
• I need SEO keywords on pages

```html
<!DOCTYPE html>
<html lang="en">
<head>
<meta charset="utf-8">
<title>Kitchen Cabinet Painting – Crestline Painting</title>
<link href="https://fonts.googleapis.com/css2?family=Roboto:wght@400;500;700&display=swap" rel="stylesheet">
<style>
:root{
  --navy:#0f4a8c;
  --navy-dark:#0b2a4f;
  --navy-deep:#0a2547;
  --red:#c8202f;
  --ink:#1d1d1d;
  --text:#666a70;
  --line:#e6e6e6;
  --soft:#f5f5f5;
  --white:#ffffff;
}
*{box-sizing:border-box;margin:0;padding:0}
html,body{width:1200px;height:3178px;overflow:hidden}
body{font-family:'Roboto',sans-serif;color:var(--text);background:var(--white);position:relative}
.abs{position:absolute}
a{color:inherit;text-decoration:none}

/* top bar */
.topbar{left:0;top:0;width:1200px;height:35px;background:var(--navy);color:#e8eef7;font-size:12px}
.topbar span{position:absolute;top:11px}
.dot{display:inline-block;width:10px;height:10px;border-radius:50%;background:#e8eef7;margin-right:6px;vertical-align:-1px}

/* header */
.header{left:0;top:35px;width:1200px;height:83px;background:var(--white);border-bottom:1px solid var(--line)}
.brand{position:absolute;font-weight:700;color:var(--navy);letter-spacing:0.5px}
.nav{position:absolute;left:356px;top:33px;font-size:13px;font-weight:500;color:var(--ink)}
.nav a{margin-right:24px}
.btn-outline{position:absolute;left:939px;top:19px;width:173px;height:46px;border:1px solid var(--red);color:var(--red);font-size:12px;font-weight:700;text-align:center;line-height:44px}

/* hero */
.hero{left:0;top:118px;width:1200px;height:273px;background:linear-gradient(90deg,#1e1e1e,#3a3a38 45%,#2a2a28)}
.hero h1{position:absolute;left:86px;top:90px;font-size:40px;font-weight:700;color:var(--white)}
.crumbs{position:absolute;left:86px;top:151px;font-size:14px;color:#eee}
.crumbs b{font-weight:500}

.ph{position:absolute}

/* content */
h2.lead{left:86px;top:878px;width:676px;font-size:21px;line-height:31px;font-weight:500;color:var(--ink)}
p.body{font-size:13.5px;line-height:26.5px;color:var(--text)}
h3.sub{font-size:21px;font-weight:500;color:var(--ink)}
.feature .num{position:absolute;left:438px;width:42px;height:42px;border-radius:50%;background:#f1f1f1;color:var(--red);font-size:20px;text-align:center;line-height:42px}
.feature h4{position:absolute;left:499px;font-size:17px;font-weight:500;color:var(--ink)}
.feature p{position:absolute;left:499px;width:245px;font-size:13.5px;line-height:26px}
.accent-block{left:86px;top:1155px;width:112px;height:132px;background:#f1f2f4}

.thumb{top:1866px;height:165px;box-shadow:0 6px 12px rgba(0,0,0,.18)}
.play{position:absolute;left:396px;top:1925px;width:48px;height:48px;border-radius:50%}

.benefit{left:86px;top:2067px;width:676px;height:366px;background:var(--soft)}
.benefit h3{position:absolute;left:44px;top:36px}
.benefit p{position:absolute;left:44px;top:78px;width:590px}
.checks{position:absolute;top:184px;font-size:13.5px;color:var(--text)}
.checks li{list-style:none;height:39.5px;position:relative;padding-left:26px}
.checks svg{position:absolute;left:0;top:2px}

/* sidebar */
.card{left:789px;width:325px;border:1px solid var(--line);background:var(--white)}
.card h3{position:absolute;left:36px;font-size:18px;font-weight:500;color:var(--ink)}
.svc{position:absolute;left:36px;width:253px;font-size:13.5px;color:#333;height:50px;line-height:50px;border-bottom:1px solid var(--line)}
.svc svg{margin-right:8px;vertical-align:1px}
.dl{position:absolute;left:36px;width:253px;height:52px;background:var(--navy-dark);color:var(--white);font-size:13.5px;font-weight:500;line-height:52px;padding-left:50px}
.dl svg{position:absolute;left:20px;top:16px}
.field{position:absolute;left:36px;width:253px;height:44px;background:var(--soft);font-size:13px;color:#888;line-height:44px;padding-left:13px}
.send{position:absolute;left:36px;width:253px;height:44px;background:var(--red);color:var(--white);font-size:13.5px;font-weight:500;text-align:center;line-height:44px}

.avail{left:789px;top:1516px;width:325px;height:561px;overflow:hidden;background:var(--navy-deep)}
.avail h3{position:absolute;left:0;width:325px;top:370px;text-align:center;color:var(--white);font-size:26px;font-weight:700}
.avail p{position:absolute;left:0;width:325px;top:426px;text-align:center;color:#c9d3e2;font-size:15.5px}
.avail .appt{position:absolute;left:44px;top:474px;width:237px;height:44px;background:var(--red);color:var(--white);font-size:15px;font-weight:500;text-align:center;line-height:44px}

/* cta */
.cta{left:0;top:2522px;width:1200px;height:169px;background:var(--red)}
.cta h2{position:absolute;left:86px;top:64px;font-size:34px;font-weight:700;color:var(--white)}
.cta .quote{position:absolute;left:947px;top:62px;width:167px;height:51px;background:var(--white);color:var(--ink);font-size:12.5px;font-weight:700;text-align:center;line-height:51px}

/* footer */
.footer{left:0;top:2691px;width:1200px;height:487px;background:linear-gradient(135deg,#0c2d56,#0e3461 55%,#0a2648)}
.flogo{position:absolute;left:80px;top:69px;width:263px;height:98px;background:var(--white)}
.footer .about{position:absolute;left:80px;top:191px;width:290px;font-size:13.5px;line-height:25px;color:#d8e0ec}
.soc{position:absolute;top:302px;width:42px;height:32px;background:#1d4475}
.soc i{position:absolute;left:17px;top:12px;width:8px;height:8px;border-radius:50%;background:#d8e0ec}
.footer h4{position:absolute;top:77px;font-size:20px;font-weight:500;color:var(--white)}
.bar{position:absolute;top:112px;width:44px;height:3px;background:var(--red)}
.flinks{position:absolute;top:146px;font-size:13.5px;color:#d8e0ec;list-style:none}
.flinks li{height:34px}
.email{position:absolute;left:788px;top:174px;width:328px;height:39px;background:#1d4475;color:#d8e0ec;font-size:13.5px;line-height:39px;padding-left:26px}
.sub-btn{position:absolute;left:788px;top:218px;width:328px;height:40px;background:var(--red);color:var(--white);font-size:13.5px;font-weight:500;text-align:center;line-height:40px}
.copy{position:absolute;left:0;width:1200px;top:445px;text-align:center;font-size:13.5px;color:#d8e0ec}
</style>
</head>
<body>

<div class="abs topbar">
  <span style="left:88px"><i class="dot"></i>E-mail: contact@crestlinepainting.com</span>
  <span style="left:336px"><i class="dot"></i>Hours: Mon-Fri: 8.00 am - 7.00 pm</span>
  <span style="left:891px"><i class="dot"></i>+ 555-014-2290</span>
  <span style="left:1021px"><i class="dot"></i><i class="dot"></i><i class="dot"></i><i class="dot"></i></span>
</div>

<header class="abs header">
  <div class="brand" style="left:99px;top:22px;font-size:28px">CRESTLINE</div>
  <nav class="nav">
    <a>Home</a><a>About</a><a>Residential</a><a>Multi-Family</a><a>Commercial</a><a>Contact</a>
  </nav>
  <a class="btn-outline">GET A FREE ESTIMATE</a>
</header>

<section class="abs hero" role="img" aria-label="Dimly lit painted kitchen with white cabinets">
  <h1>Kitchen Cabinet Painting</h1>
  <div class="crumbs">Home &nbsp;.&nbsp;&nbsp; Services &nbsp;.&nbsp;&nbsp; <b>Details</b></div>
</section>

<div class="ph" style="left:86px;top:480px;width:676px;height:373px;background:linear-gradient(180deg,#6b5a48,#b8a68c 45%,#3e342c)" role="img" aria-label="Kitchen with freshly painted white cabinets and dark island"></div>

<h2 class="abs lead">Ever wanted to give your cabinets a darker, richer look without stripping them?</h2>
<p class="abs body" style="left:86px;top:954px;width:676px">The painters at <b style="color:#333">Crestline Painting</b> can completely alter the look of your stained cabinets from a light oak or a pickled look, to a darker, richer stained look. We can give you the look of mahogany or walnut without having to strip your cabinets. We use a bonding clear primer, two coats of a customized stain-glaze and one or two varnish coats.</p>

<h3 class="abs sub" style="left:86px;top:1093px">Our Expert Painting Experts Are Available For Your Satisfaction.</h3>

<div class="abs accent-block" role="img" aria-label="Decorative accent area"></div>
<div class="ph" style="left:115px;top:1185px;width:296px;height:279px;background:linear-gradient(180deg,#5d86b8,#8a5a44 50%,#6b4a3a)" role="img" aria-label="Brick house with grey slate roof"></div>

<div class="feature">
  <div class="num" style="top:1185px">1</div>
  <h4 style="top:1188px">Durability</h4>
  <p style="top:1220px">Our systems provide a more durable, longer-lasting finish.</p>
  <div class="num" style="top:1290px">2</div>
  <h4 style="top:1293px">Installation</h4>
  <p style="top:1325px">Installs without harmful fumes or chemicals.</p>
  <div class="num" style="top:1395px">3</div>
  <h4 style="top:1398px">Protection</h4>
  <p style="top:1430px">Protects your floor from long-term UV damage.</p>
</div>

<p class="abs body" style="left:86px;top:1518px;width:676px">Next, the cabinet surfaces are cleaned to remove any oils or any other contaminants commonly found in the kitchen area. The door hardware is carefully removed or taped off to ensure a clean paint job.</p>
<p class="abs body" style="left:86px;top:1597px;width:676px">The # 1 missed preparation step by painters is what is called a prime coat. We use a special primer used to seal and prep the cabinets for a long lasting, durable top coat of premium paint.</p>

<h3 class="abs sub" style="left:86px;top:1676px">Image &amp; Video Gallery</h3>
<p class="abs body" style="left:86px;top:1719px;width:676px;font-size:13.8px">Lorem ipsum dolor sit amet, consectetur adipiscing elit, sed do eiusmod tempor incididunt ut labore et dolore magna aliqua. Ut enim ad minim veniam, quis nostrud exercitation ullamco laboris nisi ut aliquip ex ea commodo consequat. Duis aute irure dolor in reprehenderit in voluptate velit esse cillum dolore eu fugiat nulla pariatur. Excepteur sint occaecat cupidatat non proident, sunt in culpa qui officia deserunt mollit anim id est laborum.</p>

<div class="ph thumb" style="left:83px;width:213px;background:linear-gradient(160deg,#c9d3de,#3c4654 60%,#2c3440)" role="img" aria-label="Dark shingle roof on white house"></div>
<div class="ph thumb" style="left:313px;width:215px;background:linear-gradient(160deg,#8a9aa8,#2f5f9a 55%,#2a3f66)" role="img" aria-label="Worker laying roof tiles"></div>
<svg class="play" viewBox="0 0 48 48" aria-hidden="true"><circle cx="24" cy="24" r="24" fill="#c8202f"/><path d="M19 15 L33 24 L19 33 Z" fill="#fff"/></svg>
<div class="ph thumb" style="left:545px;width:213px;background:linear-gradient(160deg,#3d7fc4,#c25236 50%,#a8432d)" role="img" aria-label="Red clay roof tiles being fitted"></div>

<section class="abs benefit">
  <h3 class="sub">Benefit of Service</h3>
  <p class="body">Lorem ipsum dolor sit amet, consectetur adipiscing elit, sed do eiusmod tempor incididunt ut labore et dolore magna aliqua. Ut enim ad minim veniam, quis nostrud exercitation ullamco laboris nisi ut aliquip ex ea commodo consequat.</p>
  <ul class="checks" style="left:44px">
    <li><svg width="14" height="12" viewBox="0 0 14 12"><path d="M1 6 L5 10 L13 1" stroke="#c8202f" stroke-width="2.4" fill="none"/></svg>Lorem ipsum dolor sit amet</li>
    <li><svg width="14" height="12" viewBox="0 0 14 12"><path d="M1 6 L5 10 L13 1" stroke="#c8202f" stroke-width="2.4" fill="none"/></svg>Consectetur adipiscing elit</li>
    <li><svg width="14" height="12" viewBox="0 0 14 12"><path d="M1 6 L5 10 L13 1" stroke="#c8202f" stroke-width="2.4" fill="none"/></svg>Sed do eiusmod tempor</li>
    <li><svg width="14" height="12" viewBox="0 0 14 12"><path d="M1 6 L5 10 L13 1" stroke="#c8202f" stroke-width="2.4" fill="none"/></svg>Incididunt ut labore et dolore</li>
  </ul>
  <ul class="checks" style="left:275px">
    <li><svg width="14" height="12" viewBox="0 0 14 12"><path d="M1 6 L5 10 L13 1" stroke="#c8202f" stroke-width="2.4" fill="none"/></svg>Incididunt ut labore et dolore</li>
    <li><svg width="14" height="12" viewBox="0 0 14 12"><path d="M1 6 L5 10 L13 1" stroke="#c8202f" stroke-width="2.4" fill="none"/></svg>Sed do eiusmod tempor</li>
    <li><svg width="14" height="12" viewBox="0 0 14 12"><path d="M1 6 L5 10 L13 1" stroke="#c8202f" stroke-width="2.4" fill="none"/></svg>Consectetur adipiscing elit</li>
    <li><svg width="14" height="12" viewBox="0 0 14 12"><path d="M1 6 L5 10 L13 1" stroke="#c8202f" stroke-width="2.4" fill="none"/></svg>Lorem ipsum dolor sit amet</li>
  </ul>
</section>

<aside class="abs card" style="top:480px;height:382px">
  <h3 style="top:32px">Our Services</h3>
  <div class="svc" style="top:63px"><svg width="12" height="8" viewBox="0 0 12 8"><path d="M0 4 H10 M7 1 L11 4 L7 7" stroke="#222" stroke-width="1.5" fill="none"/></svg>Kitchen Cabinet Painting</div>
  <div class="svc" style="top:113px"><svg width="12" height="8" viewBox="0 0 12 8"><path d="M0 4 H10 M7 1 L11 4 L7 7" stroke="#222" stroke-width="1.5" fill="none"/></svg>Popcorn Removal</div>
  <div class="svc" style="top:163px"><svg width="12" height="8" viewBox="0 0 12 8"><path d="M0 4 H10 M7 1 L11 4 L7 7" stroke="#222" stroke-width="1.5" fill="none"/></svg>Drywall Repair</div>
  <div class="svc" style="top:213px"><svg width="12" height="8" viewBox="0 0 12 8"><path d="M0 4 H10 M7 1 L11 4 L7 7" stroke="#222" stroke-width="1.5" fill="none"/></svg>Gaage Floor Epoxy</div>
  <div class="svc" style="top:263px"><svg width="12" height="8" viewBox="0 0 12 8"><path d="M0 4 H10 M7 1 L11 4 L7 7" stroke="#222" stroke-width="1.5" fill="none"/></svg>Wallpaper Removal</div>
  <div class="svc" style="top:313px;border-bottom:none"><svg width="12" height="8" viewBox="0 0 12 8"><path d="M0 4 H10 M7 1 L11 4 L7 7" stroke="#222" stroke-width="1.5" fill="none"/></svg>Color Consultation</div>
</aside>

<aside class="abs card" style="top:898px;height:228px">
  <h3 style="top:32px">Download Now</h3>
  <div class="dl" style="top:79px"><svg width="14" height="18" viewBox="0 0 14 18"><path d="M1 1 H9 L13 5 V17 H1 Z" stroke="#fff" stroke-width="1.4" fill="none"/></svg>Download Document .pdf</div>
  <div class="dl" style="top:140px"><svg width="14" height="18" viewBox="0 0 14 18"><path d="M1 1 H9 L13 5 V17 H1 Z" stroke="#fff" stroke-width="1.4" fill="none"/></svg>Download Document .Word</div>
</aside>

<aside class="abs card" style="top:1163px;height:317px">
  <h3 style="top:32px">Have Any Question?</h3>
  <div class="field" style="top:79px">Name *</div>
  <div class="field" style="top:132px">E-mail *</div>
  <div class="field" style="top:185px">What's your question *</div>
  <div class="send" style="top:237px">Send</div>
</aside>

<aside class="abs avail">
  <div class="ph" style="left:0;top:0;width:325px;height:380px;background:linear-gradient(180deg,#d8d8d6,#a9a8a4 60%,#7d7b76)" role="img" aria-label="Bright two-storey entry hall with tall windows"></div>
  <svg class="ph" style="left:0;top:270px" width="325" height="291" viewBox="0 0 325 291" aria-hidden="true"><path d="M0 112 L325 0 V291 H0 Z" fill="#0a2547"/></svg>
  <h3>Available</h3>
  <p>for any type of Painting Service</p>
  <div class="appt">Make An Appointment</div>
</aside>

<section class="abs cta">
  <h2>Get Your Painting Project Started Today!</h2>
  <a class="quote">GET A QUOTE &nbsp;›</a>
</section>

<footer class="abs footer">
  <div class="flogo"><div class="brand" style="left:30px;top:30px;font-size:34px">CRESTLINE</div></div>
  <p class="about">Lorem ipsum dolor sit amet, consectetur adipiscing elit, sed do eiusmod tempor incididunt ut labore et dolore magna aliqua.</p>
  <div class="soc" style="left:80px"><i></i></div>
  <div class="soc" style="left:127px"><i></i></div>
  <div class="soc" style="left:174px"><i></i></div>
  <div class="soc" style="left:221px"><i></i></div>
  <div class="soc" style="left:268px"><i></i></div>

  <h4 style="left:432px">Quick Links</h4>
  <div class="bar" style="left:432px"></div>
  <ul class="flinks" style="left:432px"><li>Home</li><li>About Us</li><li>Residential</li><li>Commercial</li><li>Multi Family</li></ul>
  <ul class="flinks" style="left:634px"><li>Site Map</li><li>Maintenance</li><li>Repairs</li><li>Blog</li></ul>

  <h4 style="left:788px">Newsletter</h4>
  <div class="bar" style="left:788px"></div>
  <div class="flinks" style="left:788px">Subscribe For Daily Latest News &amp; Updates</div>
  <div class="email">E-mail Address</div>
  <div class="sub-btn">Subscribe Now</div>

  <div class="copy">Copyright © 2020 Crestline Painting. All Rights Reserved.</div>
</footer>

</body>
</html>
```